Quarlwick Builders Business Cards

I want to use the logo and make an unique business card that shows the textured Logo with brick and builings. I want to be able to stand out when I pass out business cards.

```html
<!DOCTYPE html>
<html lang="en">
<head>
<meta charset="utf-8">
<title>Quarlwick Builders Business Cards</title>
<link rel="stylesheet" href="https://fonts.googleapis.com/css2?family=Roboto:wght@400;700&display=swap">
<style>
  :root {
    --page-bg: #e6e6e6;
    --card-white: #ffffff;
    --panel-dark: #1b1b1b;
    --panel-dark-2: #2a2a2a;
    --text-light: #ffffff;
    --text-navy: #1c2340;
    --brick: #d9482b;
    --concrete-1: #b9b9b9;
    --concrete-2: #8d8d8d;
    --concrete-3: #5e5a57;
  }
  * { box-sizing: border-box; margin: 0; padding: 0; }
  html, body { width: 1200px; height: 1200px; overflow: hidden; }
  body {
    background: var(--page-bg);
    font-family: 'Roboto', Arial, sans-serif;
    position: relative;
  }
  .card {
    position: absolute;
    left: 139px;
    width: 922px;
    height: 526px;
    overflow: hidden;
  }
  .card-front { top: 53px; background: var(--card-white); }
  .card-back { top: 621px; }

  .front-panel {
    position: absolute; left: 0; top: 0;
    width: 442px; height: 526px;
    background: linear-gradient(160deg, var(--panel-dark-2), var(--panel-dark));
    color: var(--text-light);
  }
  .holder-name {
    position: absolute; left: 58px; top: 176px;
    font-size: 40px; font-weight: 400; letter-spacing: 0.5px;
  }
  .holder-role {
    position: absolute; left: 58px; top: 224px;
    font-size: 26px; font-weight: 400;
  }
  .divider {
    position: absolute; left: 58px; top: 287px;
    width: 384px; height: 3px; background: var(--text-light);
  }
  .contact-line {
    position: absolute; display: flex; align-items: flex-start; gap: 14px;
    font-size: 24px; line-height: 31px;
  }
  .contact-line svg { flex: none; margin-top: 5px; }
  .front-panel .contact-line { left: 58px; }
  .line-phone { top: 369px; }
  .line-web { top: 413px; }

  .logo-tile {
    position: absolute; left: 551px; top: 0;
    width: 306px; height: 330px;
    background: radial-gradient(circle at 50% 45%, #7d7a77, #4a4846 75%, #353433);
    display: flex; flex-direction: column; align-items: center; justify-content: center;
    gap: 14px; text-align: center;
  }
  .logo-name {
    color: var(--brick); font-weight: 700; text-transform: uppercase;
  }
  .logo-tile .logo-name { font-size: 30px; line-height: 34px; }
  .service-list { color: #1f2b57; font-weight: 700; }
  .logo-tile .service-list { font-size: 11px; color: #dfe3ee; }

  .front-contacts { color: var(--text-navy); }
  .front-contacts .contact-line { left: 495px; }
  .line-email { top: 369px; }
  .line-address { top: 413px; }

  .back-texture {
    position: absolute; inset: 0;
    background:
      radial-gradient(ellipse at 20% 30%, rgba(255,255,255,0.35), transparent 55%),
      radial-gradient(ellipse at 85% 75%, rgba(120,90,70,0.35), transparent 55%),
      linear-gradient(135deg, var(--concrete-1), var(--concrete-2) 60%, var(--concrete-3));
  }
  .back-logo {
    position: absolute; left: 230px; top: 55px;
    width: 462px; height: 420px;
    display: flex; flex-direction: column; align-items: center; justify-content: center; gap: 40px;
    text-align: center;
  }
  .back-logo .logo-name { font-size: 56px; line-height: 62px; }
  .back-logo .service-list { font-size: 19px; }
</style>
</head>
<body>
  <section class="card card-front">
    <div class="front-panel" role="img" aria-label="Dark black brick wall texture">
      <h1 class="holder-name">DORREN VASQUELL</h1>
      <p class="holder-role">Owner</p>
      <div class="divider"></div>
      <div class="contact-line line-phone">
        <svg width="16" height="22" viewBox="0 0 16 22"><rect x="2" y="1" width="12" height="20" rx="2" fill="none" stroke="#fff" stroke-width="2"/><rect x="6" y="16" width="4" height="2" fill="#fff"/></svg>
        <span>928-555-0147</span>
      </div>
      <div class="contact-line line-web">
        <svg width="20" height="20" viewBox="0 0 20 20"><circle cx="10" cy="10" r="8" fill="none" stroke="#fff" stroke-width="2"/><path d="M2 10h16M10 2c3 3 3 13 0 16M10 2c-3 3-3 13 0 16" fill="none" stroke="#fff" stroke-width="1.6"/></svg>
        <span>www.quarlwick.com</span>
      </div>
    </div>

    <div class="logo-tile" role="img" aria-label="Company logo area on weathered concrete backdrop">
      <span class="logo-name">Quarlwick<br>Builders</span>
      <span class="service-list">Patios - Sidewalks - Retaining Walls - Foundations</span>
    </div>

    <div class="front-contacts">
      <div class="contact-line line-email">
        <svg width="22" height="18" viewBox="0 0 22 18"><rect x="1" y="2" width="20" height="14" rx="1.5" fill="#1c2340"/><path d="M2 4l9 6 9-6" fill="none" stroke="#fff" stroke-width="1.8"/></svg>
        <span>info@quarlwick.com</span>
      </div>
      <div class="contact-line line-address">
        <svg width="18" height="24" viewBox="0 0 18 24"><path d="M9 1C4.6 1 1 4.5 1 8.9 1 15 9 23 9 23s8-8 8-14.1C17 4.5 13.4 1 9 1z" fill="#1c2340"/><circle cx="9" cy="9" r="3" fill="#fff"/></svg>
        <span>48 Stonefield Road, Ridgecrest Bay,<br>AZ 12345</span>
      </div>
    </div>
  </section>

  <section class="card card-back">
    <div class="back-texture" role="img" aria-label="Weathered grey concrete wall texture"></div>
    <div class="back-logo">
      <span class="logo-name">Quarlwick<br>Builders</span>
      <span class="service-list">Patios - Sidewalks - Retaining Walls - Foundations</span>
    </div>
  </section>
</body>
</html>
```